Non-profit wants to save the world needs Wordpress presence

My name is Marco Estelani. I'm a photographer who started a charity (Rancho las Brisas) to help the rural schools and health clinics in Central America. We distribute schools supplies and help health clinics with much needed medical supplies and equipment. I need a way to accept donations. I need to have several different writers post to the blog (in Spanish and English). I have a domain name registered (www.rancholasbrisas.org) and started a simple wordpress site as well at http://www.rancholasbrisas.wordpress.com

Industry/Entity Type

Charity

```html
<!DOCTYPE html>
<html lang="en">
<head>
<meta charset="utf-8">
<title>Rancho las Brisas</title>
<link href="https://fonts.googleapis.com/css2?family=Oswald:wght@400;500&family=Open+Sans:ital,wght@0,400;0,600;0,700;1,400;1,600&display=swap" rel="stylesheet">
<style>
:root{
  --red:#d71f26;
  --orange:#ee8422;
  --green:#4e9a3a;
  --lime:#7dbb35;
  --purple:#8e2a92;
  --charcoal:#454545;
  --ink:#333;
  --text:#666;
  --page:#f1f1f1;
  --band:#e6e6e6;
  --footer:#3b3b3b;
  --bottom:#252525;
}
*{margin:0;padding:0;box-sizing:border-box}
html,body{width:683px;height:1200px;overflow:hidden}
body{position:relative;background:var(--page);font-family:"Open Sans",sans-serif;color:var(--text)}
.abs{position:absolute}
.head-font{font-family:"Oswald",sans-serif}

/* header */
.site-header{left:0;top:0;width:683px;height:59px;background:#fff;border-bottom:2px solid var(--red)}
.brand{left:100px;top:8px;display:flex;align-items:center;gap:5px}
.brand-dot{width:14px;height:14px;border-radius:50%;background:var(--lime)}
.brand-name{font-family:"Oswald",sans-serif;font-size:13px;font-weight:500;color:var(--green);line-height:1.05;width:58px}
.volunteer-btn{left:412px;top:14px;width:66px;height:11px;border-radius:6px;background:var(--red);color:#fff;font-family:"Oswald",sans-serif;font-size:6.5px;line-height:11px;text-align:center}
.lang-select{left:485px;top:14px;width:57px;height:11px;border-radius:6px;background:#e2e2e2;color:#555;font-family:"Oswald",sans-serif;font-size:6px;line-height:11px;padding-left:6px}
.lang-select::after{content:"▾";position:absolute;right:5px}
.social-top{left:548px;top:14px;display:flex;gap:2px}
.social-top span{width:10px;height:10px;border-radius:50%;background:#555}
.main-nav{left:221px;top:40px;display:flex;gap:0}
.main-nav a{font-family:"Oswald",sans-serif;font-size:8.2px;color:#333;text-decoration:none;margin-right:13px}
.main-nav a.active{color:var(--red)}
.search{left:498px;top:36px;width:84px;height:18px;border:1px solid #ddd;border-radius:9px;font-size:6px;color:#aaa;line-height:16px;padding-left:9px}
.search svg{position:absolute;right:7px;top:4px}

/* hero */
.hero{left:0;top:61px;width:683px;height:249px;background:linear-gradient(120deg,#c99a7a,#9d7a62 35%,#6d8aa8 60%,#b59988);}
.hero-caption{left:348px;top:156px;width:234px;height:57px;background:rgba(214,111,14,.9);color:#fff;font-family:"Oswald",sans-serif;font-size:13.5px;line-height:16px;padding:12px 0 0 19px}
.hero-dots{left:328px;top:291px;display:flex;gap:2px}
.hero-dots span{width:7px;height:7px;border-radius:50%;background:var(--red)}
.hero-dots span:nth-child(2){background:var(--orange)}
.orange-rule{left:0;top:310px;width:683px;height:2px;background:var(--orange)}
.intro-band{left:0;top:312px;width:683px;height:54px;background:var(--green);color:#fff}
.intro-band .slogan{position:absolute;left:114px;top:11px;font-style:italic;font-size:10.3px}
.intro-band .lead{position:absolute;left:112px;top:31px;font-size:7px}
.help-btn{left:524px;top:29px;width:49px;height:14px;border:1px solid #b9dca2;border-radius:2px;background:#68ad45;font-family:"Oswald",sans-serif;font-size:7px;line-height:12px;text-align:center;color:#fff}

/* what we do */
.section-title{left:100px;top:378px;width:482px;text-align:center;font-family:"Oswald",sans-serif;font-size:12.5px;color:#333}
.section-title::before,.section-title::after{content:"";position:absolute;top:9px;width:200px;height:1px;background:#d6d6d6}
.section-title::before{left:0}.section-title::after{right:0}
.what-lead{left:100px;top:413px;width:482px;text-align:center;font-style:italic;font-size:6.6px;line-height:11px;color:#555}
.service{top:452px;width:90px;text-align:center}
.service .disc{width:76px;height:76px;border-radius:50%;margin:0 auto;display:flex;align-items:center;justify-content:center}
.service p{margin-top:10px;font-size:8.3px;font-weight:600}
.divider-shadow{left:100px;top:572px;width:482px;height:4px;background:radial-gradient(ellipse at center,rgba(0,0,0,.1),transparent 70%)}

/* cards */
.card{top:594px;width:150px;height:195px;background:#fff;border:1px solid #e2e2e2;text-align:center}
.card h3{height:24px;background:var(--red);color:#fff;font-family:"Oswald",sans-serif;font-weight:400;font-size:10px;line-height:24px;margin:-1px -1px 0}
.card .photo{width:135px;height:57px;margin:8px auto 0}
.card p{font-size:6.6px;line-height:10.5px;color:#666;padding:8px 10px 0}
.card .btn{display:block;width:74px;height:21px;margin:12px auto 0;background:var(--red);color:#fff;font-family:"Open Sans",sans-serif;font-weight:700;font-size:7px;line-height:21px}

/* lower band */
.lower-band{left:0;top:810px;width:683px;height:192px;background:var(--band)}
.block-title{font-family:"Oswald",sans-serif;font-size:12.5px;color:#333;top:823px}
.block-rule{top:842px;height:1px;background:#cfcfcf}
.arrows{top:825px;display:flex;gap:2px}
.arrows span{width:12px;height:12px;background:#fff;border:1px solid #ccc;font-size:7px;line-height:10px;text-align:center;color:#555}
.post{top:854px;width:98px}
.post .thumb{height:58px}
.post h4{font-size:7.6px;font-weight:600;color:#333;margin-top:6px}
.post .date{font-size:6px;color:var(--orange);margin-top:1px}
.post p{font-size:6.4px;line-height:9.6px;margin-top:2px}
.post .more{font-size:6.4px;font-weight:700;color:var(--red);margin-top:3px}
.quote-box{left:364px;top:853px;width:218px;height:77px;background:#fff}
.quote-box::after{content:"";position:absolute;left:24px;bottom:-6px;border:6px solid transparent;border-top-color:#fff;border-bottom:0}
.avatar{left:20px;top:18px;width:38px;height:38px;border-radius:50%;background:radial-gradient(circle,#c9d7de,#8fa9b5)}
.quote-box p{position:absolute;left:65px;top:17px;width:140px;font-style:italic;font-size:6.4px;line-height:10px;color:#666}
.quote-name{left:364px;top:940px;font-style:italic;font-weight:600;font-size:7.6px;color:#444}
.quote-btn{left:364px;top:960px;width:60px;height:17px;background:var(--red);color:#fff;font-weight:700;font-size:7px;line-height:17px;text-align:center}

/* partners */
.partners{left:0;top:1002px;width:683px;height:52px;background:#efefef}
.badge{top:1011px;height:34px;background:#bbb}

/* footer */
.site-footer{left:0;top:1054px;width:683px;height:127px;background:var(--footer);color:#ddd}
.footer-brand{left:102px;top:1082px;width:84px;height:70px;display:flex;align-items:center;gap:5px}
.footer-brand .dot{width:16px;height:16px;border-radius:50%;background:#666}
.footer-brand span{font-family:"Oswald",sans-serif;font-size:14px;color:#bbb;line-height:1.1}
.footer-links{left:222px;top:1075px;list-style:none}
.footer-links li{font-size:5.8px;line-height:11.2px;color:#ddd}
.footer-links li::before{content:"›";color:var(--lime);font-weight:700;margin-right:5px;font-size:8px}
.foot-head{font-weight:700;font-size:7.4px;color:#eee}
.contact-line{left:320px;font-size:6.6px;color:#ccc;display:flex;align-items:center;gap:4px}
.contact-line.mail{color:var(--lime)}
.foot-social{left:320px;top:1143px;display:flex;gap:3px}
.foot-social span{width:15px;height:15px;border-radius:50%;background:#888}
.news-text{left:446px;top:1090px;width:130px;font-style:italic;font-size:6.4px;line-height:9.6px;color:#ccc}
.news-input{left:446px;top:1113px;width:126px;height:18px;background:#e8e8e8;color:#777;font-size:6px;line-height:18px;padding-left:9px}
.news-submit{left:446px;top:1138px;width:51px;height:19px;background:var(--lime);color:#fff;font-weight:700;font-size:7px;line-height:19px;text-align:center}
.copyright{left:0;top:1181px;width:683px;height:19px;background:var(--bottom);color:#888;font-size:5.8px;line-height:19px;text-align:center}
</style>
</head>
<body>

<header class="abs site-header">
  <div class="abs brand"><span class="brand-dot"></span><span class="brand-name">Rancho las Brisas</span></div>
  <div class="abs volunteer-btn">› Volunteer to a mission</div>
  <div class="abs lang-select">Select a Language</div>
  <div class="abs social-top"><span></span><span></span><span></span></div>
  <nav class="abs main-nav">
    <a class="active" href="#">HOME</a><a href="#">ABOUT US</a><a href="#">MISSION</a><a href="#">MEDIA</a><a href="#">HELP</a><a href="#">NEWS</a><a href="#">BLOG</a><a href="#">CONTACT</a>
  </nav>
  <div class="abs search">Search...
    <svg width="8" height="8" viewBox="0 0 10 10"><circle cx="4" cy="4" r="3" fill="none" stroke="#aaa" stroke-width="1.4"/><line x1="6.3" y1="6.3" x2="9.3" y2="9.3" stroke="#aaa" stroke-width="1.4"/></svg>
  </div>
</header>

<div class="abs hero" role="img" aria-label="Photo of smiling children gathered around a volunteer in a schoolyard"></div>
<div class="abs hero-caption">DEVELOP LITERACY, BASIC EDUCATION<br>AND VOCATIONAL TRAINING.</div>
<div class="abs hero-dots"><span></span><span></span><span></span></div>
<div class="abs orange-rule"></div>

<section class="abs intro-band">
  <p class="slogan">Humanitarian and international NGO <b>Rancho las Brisas</b> with baseline as “Towards the save world”</p>
  <p class="lead">Lorem ipsum dolor sit amet, consectetur adipiscing elit. Suspendisse faucibus venenatis orci, vitae porta lacus vehicula a.</p>
  <div class="abs help-btn">HELP US</div>
</section>

<h2 class="abs section-title" style="font-weight:400">WHAT WE DO</h2>
<p class="abs what-lead">Lorem ipsum dolor sit amet, consectetur adipiscing elit. Suspendisse faucibus venenatis orci, vitae porta lacus vehicula a. Vivamus convallis faucibus nibh eu condimentum. Donec mattis ut ex in suscipit. Mauris pulvinar tortor nisl, quis efficitur nunc tristique sit amet. Proin dignissim, turpis eget porta accumsan,</p>

<div class="abs service" style="left:93px">
  <div class="disc" style="background:var(--green)"><svg width="34" height="34" viewBox="0 0 34 34"><path d="M6 8l10 3v18L6 26z M18 11l10-3v18l-10 3z" fill="#fff"/></svg></div>
  <p style="color:var(--green)">Education</p>
</div>
<div class="abs service" style="left:195px">
  <div class="disc" style="background:var(--orange)"><svg width="34" height="34" viewBox="0 0 34 34"><rect x="5" y="10" width="24" height="17" rx="2" fill="#fff"/><rect x="13" y="6" width="8" height="5" fill="none" stroke="#fff" stroke-width="2"/><path d="M15.5 14h3v3h3v3h-3v3h-3v-3h-3v-3h3z" fill="var(--orange)"/></svg></div>
  <p style="color:var(--orange)">Health</p>
</div>
<div class="abs service" style="left:297px">
  <div class="disc" style="background:var(--purple)"><svg width="34" height="34" viewBox="0 0 34 34"><path d="M17 5C14 11 10 16 10 21a7 7 0 0014 0c0-5-4-10-7-16z" fill="#fff"/></svg></div>
  <p style="color:var(--purple)">Water &amp; Energy</p>
</div>
<div class="abs service" style="left:398px">
  <div class="disc" style="background:var(--red)"><svg width="34" height="34" viewBox="0 0 34 34"><rect x="7" y="21" width="4" height="7" fill="#fff"/><rect x="13" y="17" width="4" height="11" fill="#fff"/><rect x="19" y="19" width="4" height="9" fill="#fff"/><rect x="25" y="13" width="4" height="15" fill="#fff"/><path d="M7 17l7-6 5 3 8-8" fill="none" stroke="#fff" stroke-width="2"/><path d="M24 5h5v5z" fill="#fff"/></svg></div>
  <p style="color:var(--red)">Economic Activities</p>
</div>
<div class="abs service" style="left:500px">
  <div class="disc" style="background:var(--charcoal)"><svg width="36" height="34" viewBox="0 0 36 34"><circle cx="10" cy="12" r="4" fill="#fff"/><circle cx="26" cy="12" r="4" fill="#fff"/><circle cx="18" cy="10" r="5" fill="#fff"/><path d="M3 25c0-5 3-8 7-8s7 3 7 8z M19 25c0-5 3-8 7-8s7 3 7 8z" fill="#fff"/><path d="M9 26c0-6 4-10 9-10s9 4 9 10z" fill="#fff"/></svg></div>
  <p style="color:#333">Social Activities</p>
</div>

<div class="abs divider-shadow"></div>

<article class="abs card" style="left:100px">
  <h3>OUR MISSION</h3>
  <div class="photo" role="img" aria-label="Photo of a photographer with children on a forest path" style="background:linear-gradient(135deg,#7d8f5c,#a7a58c 55%,#5f7346)"></div>
  <p>Aenean eget ligula interdum, mollis turpis non, posuere lorem. Sed sodales fringilla sapien id tristique. Mauris sed erat urna. Morbi nec urna lobortis, euismod sapien nec, tempor orci.</p>
  <span class="btn">LEARN MORE +</span>
</article>
<article class="abs card" style="left:266px">
  <h3>BECOME VOLUNTEER</h3>
  <div class="photo" role="img" aria-label="Photo of three smiling volunteers in blue shirts" style="background:linear-gradient(90deg,#f4ede8,#3f7fc4 30%,#2e6db4 50%,#4a86c8 75%,#f3ece6)"></div>
  <p>Aenean eget ligula interdum, mollis turpis non, posuere lorem. Sed sodales fringilla sapien id tristique. Mauris sed erat urna. Morbi nec urna lobortis, euismod sapien nec, tempor orci.</p>
  <span class="btn">LEARN MORE +</span>
</article>
<article class="abs card" style="left:433px">
  <h3>HELP SAVE WORLD</h3>
  <div class="photo" role="img" aria-label="Photo of hands holding a small globe over green grass" style="background:radial-gradient(circle at 50% 50%,#4d7fb4 0,#5d8e5a 22%,#6fb33d 55%,#3f8a2a)"></div>
  <p>Aenean eget ligula interdum, mollis turpis non, posuere lorem. Sed sodales fringilla sapien id tristique. Mauris sed erat urna. Morbi nec urna lobortis, euismod sapien nec, tempor orci.</p>
  <span class="btn">LEARN MORE +</span>
</article>

<div class="abs lower-band"></div>
<h2 class="abs block-title" style="left:100px;font-weight:400">RECENT BLOGS</h2>
<div class="abs block-rule" style="left:100px;width:220px"></div>
<div class="abs arrows" style="left:295px"><span>‹</span><span>›</span></div>

<article class="abs post" style="left:100px">
  <div class="thumb" role="img" aria-label="Photo of a hand catching water from a tap" style="background:linear-gradient(135deg,#9fb77f,#d2c3ad 60%,#a89b8a)"></div>
  <h4>Cras vehicula, lectus ut...</h4>
  <div class="date">▣ 25-09-2014</div>
  <p>Aenean eget ligula interdum, mollis turpis non, posuere lorem. Sed sodales fringilla sapien id tristique.</p>
  <div class="more">Read More +</div>
</article>
<article class="abs post" style="left:221px">
  <div class="thumb" role="img" aria-label="Photo of a girl holding a drawing in a park" style="background:linear-gradient(135deg,#6f9e3f,#a6c27a 55%,#4f7f2f)"></div>
  <h4>Cras vehicula, lectus ut...</h4>
  <div class="date">▣ 25-09-2014</div>
  <p>Aenean eget ligula interdum, mollis turpis non, posuere lorem. Sed sodales fringilla sapien id tristique.</p>
  <div class="more">Read More +</div>
</article>

<h2 class="abs block-title" style="left:362px;font-weight:400">TESTIMONIALS</h2>
<div class="abs block-rule" style="left:362px;width:190px"></div>
<div class="abs arrows" style="left:558px"><span>‹</span><span>›</span></div>
<div class="abs quote-box">
  <div class="abs avatar" role="img" aria-label="Portrait photo of the reviewer"></div>
  <p>Aenean eget ligula interdum, mollis turpis non, posuere lorem. Sed sodales fringilla sapien id tristique. Mauris sed erat urna. Morbi nec urna lobortis, euismod sapien nec, tempor orci.</p>
</div>
<div class="abs quote-name">Lina Caravel</div>
<div class="abs quote-btn">READ MORE +</div>

<div class="abs partners"></div>
<div class="abs badge" style="left:140px;width:48px;border-radius:50%"></div>
<div class="abs badge" style="left:208px;width:30px;border-radius:50%"></div>
<div class="abs badge" style="left:262px;width:80px;height:20px;top:1018px"></div>
<div class="abs badge" style="left:358px;width:62px;height:30px;top:1013px"></div>
<div class="abs badge" style="left:441px;width:46px;height:24px;top:1016px"></div>
<div class="abs badge" style="left:502px;width:36px"></div>

<footer class="abs site-footer"></footer>
<div class="abs footer-brand"><span class="dot"></span><span>Rancho las Brisas</span></div>
<ul class="abs footer-links">
  <li>HOME</li><li>ABOUT US</li><li>MISSION</li><li>MEDIA</li><li>HELP</li><li>NEWS</li><li>BLOG</li><li>CONTACT</li>
</ul>
<div class="abs foot-head" style="left:320px;top:1073px">QUICK CONTACT INFO :</div>
<div class="abs contact-line" style="top:1089px"><svg width="7" height="8" viewBox="0 0 7 9"><path d="M3.5 0A3.3 3.3 0 000 3.4C0 6 3.5 9 3.5 9S7 6 7 3.4A3.3 3.3 0 003.5 0z" fill="#ccc"/><circle cx="3.5" cy="3.4" r="1.2" fill="#3b3b3b"/></svg>48, Harbor Lane Suite 2</div>
<div class="abs contact-line" style="top:1101px"><svg width="7" height="8" viewBox="0 0 8 8"><path d="M1 0l2 2-1 1.3a5 5 0 002.7 2.7L6 5l2 2-1 1C3 8 0 5 0 1z" fill="#ccc"/></svg>P (555) 014-2231</div>
<div class="abs contact-line mail" style="top:1113px"><svg width="7" height="6" viewBox="0 0 8 6"><rect width="8" height="6" fill="#ccc"/><path d="M0 0l4 3 4-3" fill="none" stroke="#3b3b3b"/></svg>info@rancholasbrisas.org</div>
<div class="abs foot-head" style="left:320px;top:1129px">FOLLOW US :</div>
<div class="abs foot-social"><span></span><span></span><span></span></div>
<div class="abs foot-head" style="left:446px;top:1073px">SIGNUP NEWSLETTER</div>
<p class="abs news-text">Aenean eget ligula interdum, mollis turpis non, posuere lorem.</p>
<div class="abs news-input">Enter Email Address</div>
<div class="abs news-submit">SUBMIT</div>
<div class="abs copyright">Copyright © 2014 Rancho las Brisas. All rights Reserved</div>

</body>
</html>
```